Harborline Energy - needs a business card

Harborline Energy is a U.S. based diesel sourcing and distribution company that supports American oil & gas fields through providing quality product and consistent services.

Target Market(s)

Oil and Gas

Contact Information for Business Card

The background of the card must be white to ensure the logo pops.

Font styles to use
Serif
Sans Serif

Colors

Designer to choose colors to be used in the design.

Requirements
Must have
• Front of Card: Tag line: Harborline Energy, Powering America's Oil & Gas fields.
• Not sure if you guys do this part but just in case...
• Dale Menschow
• Owner/CEO
• C:555.318.4076
• E:Dmenschow@harborlineenergy.example
• W:Harborlineenergy.example
• Locations: Servicing the Powder River, DJ basin and Bakken formations.
• Back of Card: " Frac fueling is what we do. We understand how important diesel fuel is to your operation, which is why our main service line is Frac fueling. We assure our supply and stand by our service"

```html
<!DOCTYPE html>
<html lang="en">
<head>
<meta charset="utf-8">
<title>Harborline Energy – Business Card</title>
<link rel="stylesheet" href="https://fonts.googleapis.com/css2?family=Roboto:wght@400;500;700&family=Roboto+Condensed:wght@700&display=swap">
<style>
  :root {
    --navy: #1f3566;
    --red: #c8202f;
    --paper: #fbfaf7;
    --backdrop: #e9e7e3;
    --text: #243a6b;
  }
  * { box-sizing: border-box; margin: 0; padding: 0; }
  html, body {
    width: 907px; height: 1200px; overflow: hidden;
    background: var(--backdrop);
    font-family: "Roboto", Arial, sans-serif;
    color: var(--text);
  }
  .sheet {
    width: 907px; height: 1200px;
    display: flex; flex-direction: column; align-items: center; justify-content: center;
    gap: 110px;
  }
  .card {
    position: relative;
    width: 770px; height: 440px;
    background: var(--paper);
    box-shadow: 0 6px 18px rgba(0,0,0,0.12);
  }
  /* Front */
  .card-front { display: flex; align-items: center; }
  .brand-panel {
    width: 50%; height: 100%;
    display: flex; flex-direction: column; align-items: center; justify-content: center;
    text-align: center; padding: 0 30px;
  }
  .brand-mark { display: flex; align-items: center; gap: 14px; }
  .brand-dot {
    width: 46px; height: 46px; border-radius: 50%;
    background: var(--navy);
  }
  .brand-name {
    font-family: "Roboto Condensed", "Arial Narrow", sans-serif;
    font-weight: 700; font-size: 40px; line-height: 1;
    color: var(--navy); letter-spacing: 0.5px;
  }
  .tagline {
    margin-top: 22px;
    font-size: 19px; line-height: 1.35; color: var(--text);
  }
  .divider {
    width: 4px; height: 250px; background: var(--navy); border-radius: 2px;
  }
  .contact-panel {
    width: 50%; height: 100%;
    display: flex; flex-direction: column; justify-content: center;
    padding: 0 34px 0 36px;
  }
  .person-name {
    font-family: "Roboto Condensed", "Arial Narrow", sans-serif;
    font-weight: 700; font-size: 34px; color: var(--red); line-height: 1.05;
  }
  .person-title {
    display: inline-block; margin-top: 4px;
    font-family: "Roboto Condensed", "Arial Narrow", sans-serif;
    font-weight: 700; font-size: 23px; color: var(--navy);
    padding-bottom: 4px; border-bottom: 5px solid var(--navy);
    align-self: flex-start; padding-right: 40px;
  }
  .contact-list {
    list-style: none; margin-top: 46px;
    font-size: 17px; line-height: 1.45; color: var(--text);
  }
  /* Back */
  .card-back {
    display: flex; flex-direction: column; align-items: center;
  }
  .card-back .brand-mark { margin-top: 150px; }
  .card-back .brand-name { font-size: 46px; }
  .card-back .brand-dot { width: 52px; height: 52px; }
  .service-quote {
    position: absolute; left: 40px; right: 40px; bottom: 44px;
    font-size: 15px; line-height: 1.4; color: var(--text); text-align: left;
  }
</style>
</head>
<body>
<main class="sheet">
  <section class="card card-front" aria-label="Business card front">
    <div class="brand-panel">
      <div class="brand-mark">
        <span class="brand-dot"></span>
        <span class="brand-name">Harborline Energy</span>
      </div>
      <p class="tagline">Harborline Energy<br>Powering America's Oil &amp; Gas fields</p>
    </div>
    <div class="divider"></div>
    <div class="contact-panel">
      <h1 class="person-name">Dale Menschow</h1>
      <h2 class="person-title">Owner/CEO</h2>
      <ul class="contact-list">
        <li>C: 555.318.4076</li>
        <li>E: Dmenschow@harborlineenergy.example</li>
        <li>W: Harborlineenergy.example</li>
        <li>Locations: Servicing the Powder River<br>DJ basin and Bakken formations</li>
      </ul>
    </div>
  </section>

  <section class="card card-back" aria-label="Business card back">
    <div class="brand-mark">
      <span class="brand-dot"></span>
      <span class="brand-name">Harborline Energy</span>
    </div>
    <p class="service-quote">" Frac fueling is what we do. We understand how important diesel fuel is to your operation, which is why our main service line is Frac fueling. We assure our supply and stand by our service"</p>
  </section>
</main>
</body>
</html>
```